Design for supplement packages

We are developing a new supplement brand are looking for a label, based on the design of our naturopath practice. It should include our logo, the basic colors are green, gold and white. www.haus-solvarin.de is the practices web site.

Target Market(s)

Europe and North America

Industry/Entity Type

Supplement

Font styles to use
Sans Serif

Colors
acd037
ffffff

Requirements
Should not have
• A too busy design. I like it simple and high class

```html
<!DOCTYPE html>
<html lang="en">
<head>
<meta charset="utf-8">
<title>Haus Solvarin – Holistic Supplement Label</title>
<link rel="stylesheet" href="https://fonts.googleapis.com/css2?family=Josefin+Sans:wght@300;400&family=Josefin+Slab:wght@400&display=swap">
<style>
  :root {
    --backdrop: #ececee;
    --label-white: #ffffff;
    --leaf-green: #acd037;
    --deep-green: #86a232;
    --gold: #b8965a;
    --taupe: #7d756c;
  }
  html, body {
    margin: 0;
    width: 1200px;
    height: 900px;
    overflow: hidden;
    background: var(--backdrop);
  }
  .canvas {
    position: relative;
    width: 1200px;
    height: 900px;
  }
  .label {
    position: absolute;
    left: 200px;
    top: 150px;
    width: 800px;
    height: 600px;
    background: var(--label-white);
    box-shadow: 0 6px 30px rgba(0,0,0,0.08);
    overflow: hidden;
  }
  .label-shapes {
    position: absolute;
    inset: 0;
  }
  .brand {
    position: absolute;
    top: 150px;
    left: 0;
    right: 0;
    display: flex;
    justify-content: center;
    align-items: center;
    gap: 18px;
  }
  .brand-dot {
    width: 34px;
    height: 34px;
    border-radius: 50%;
    background: var(--leaf-green);
  }
  .brand-name {
    font-family: "Josefin Sans", sans-serif;
    font-weight: 300;
    font-size: 56px;
    letter-spacing: 1px;
    color: var(--deep-green);
  }
  .product-title {
    position: absolute;
    top: 300px;
    left: 0;
    right: 0;
    text-align: center;
    font-family: "Josefin Slab", serif;
    font-size: 42px;
    line-height: 1.15;
    letter-spacing: 3px;
    color: var(--taupe);
    margin: 0;
    font-weight: 400;
  }
  .divider {
    position: absolute;
    left: 50%;
    width: 150px;
    margin-left: -75px;
    border-top: 3px dotted var(--leaf-green);
  }
  .divider-top { top: 280px; }
  .divider-bottom { top: 410px; }
  .count {
    position: absolute;
    bottom: 40px;
    left: 0;
    right: 0;
    text-align: center;
    font-family: "Josefin Slab", serif;
    font-size: 24px;
    letter-spacing: 2px;
    color: #e9f1cc;
  }
</style>
</head>
<body>
<main class="canvas">
  <section class="label">
    <svg class="label-shapes" width="800" height="600" viewBox="0 0 800 600" aria-hidden="true">
      <defs>
        <linearGradient id="bandShade" x1="0" y1="0" x2="1" y2="0">
          <stop offset="0" stop-color="#acd037"/>
          <stop offset="1" stop-color="#8ea935"/>
        </linearGradient>
      </defs>
      <path d="M0 60 Q400 130 800 60" fill="none" stroke="var(--gold)" stroke-width="3"/>
      <path d="M0 380 Q400 470 800 380 L800 600 L0 600 Z" fill="url(#bandShade)"/>
      <path d="M0 540 Q400 610 800 540" fill="none" stroke="var(--gold)" stroke-width="3"/>
      <path d="M0 380 Q400 470 800 380" fill="none" stroke="var(--gold)" stroke-width="2"/>
    </svg>

    <div class="brand">
      <span class="brand-dot"></span>
      <span class="brand-name">Haus Solvarin</span>
    </div>

    <div class="divider divider-top"></div>
    <h1 class="product-title">HOLISTIC<br>SUPPLEMENT</h1>
    <div class="divider divider-bottom"></div>

    <p class="count">60 capsules</p>
  </section>
</main>
</body>
</html>
```